Ward Compass Business Card Design*

We need a business card design for our company Ward Compass. Our company is specialized in providing online consulting services regarding medical institutions, hospitals and doctors. We work with patients worldwide looking to choose between healthcare providers. We have a website you may use as a reference, where we list doctors and clinics worldwide. So we target Medical providers as well as patients worldwide.
Target Market(s)
Medical Providers and patients around the world
Industry/Entity Type
Medical
Contact Information for Business Card
Salma Derkaoui
CEO
+90 612 348 2071
info@wardcompass-example.com
www.wardcompass-example.com
14 Annakhil 3 H.R.B. Rabat, Morocco
Requirements
Must have
- Company logo/name on one full side, personal info and smaller logo and company name on the other side.
Nice to have
- Smart and elegant design

```html
<!DOCTYPE html>
<html lang="en">
<head>
<meta charset="utf-8">
<title>Ward Compass — Business Card</title>
<link href="https://fonts.googleapis.com/css2?family=Lato:wght@400;700&display=swap" rel="stylesheet">
<style>
  :root {
    --navy: #163a63;
    --grey: #8a8b8d;
    --grey-light: #c9ced6;
    --paper: #f7f7f5;
    --backdrop: #6b6b6b;
    --ink-light: #e9edf2;
  }
  * { box-sizing: border-box; margin: 0; padding: 0; }
  html, body {
    width: 1200px; height: 1056px; overflow: hidden;
    background: var(--backdrop);
    font-family: 'Lato', sans-serif;
  }
  .canvas { position: relative; width: 1200px; height: 1056px; }

  .card {
    position: absolute;
    width: 700px; height: 400px;
    background: var(--paper);
    overflow: hidden;
    box-shadow: 0 10px 30px rgba(0,0,0,0.3);
  }
  .card--front { left: 250px; top: 96px; }
  .card--back  { left: 250px; top: 560px; }

  .card__panel { position: absolute; inset: 0; }

  .brand {
    position: absolute;
    display: flex; align-items: center; gap: 12px;
  }
  .brand__dot {
    border-radius: 50%;
    background: var(--navy);
  }
  .brand__name {
    color: var(--navy);
    font-weight: 700;
    letter-spacing: 0.02em;
    text-transform: uppercase;
  }
  .card--front .brand { left: 48px; top: 92px; }
  .card--front .brand__dot { width: 38px; height: 38px; }
  .card--front .brand__name { font-size: 21px; }

  .card--back .brand { left: 50%; top: 50%; transform: translate(-50%, -50%); }
  .card--back .brand__dot { width: 50px; height: 50px; }
  .card--back .brand__name { font-size: 28px; }

  .details {
    position: absolute;
    right: 34px; top: 104px;
    text-align: right;
    color: var(--ink-light);
  }
  .details__name {
    font-size: 32px; font-weight: 700;
    letter-spacing: 0.01em; text-transform: uppercase;
    color: var(--grey-light);
  }
  .details__role {
    font-size: 13px; color: var(--grey);
    margin-top: -2px; margin-right: 2px;
  }
  .contact { list-style: none; margin-top: 16px; }
  .contact__item {
    display: flex; justify-content: flex-end; align-items: center;
    gap: 12px; font-size: 15px; line-height: 23px;
  }
  .contact__icon { width: 13px; height: 13px; fill: var(--grey); flex: none; }
  .details__address {
    position: absolute; right: 34px; bottom: 78px;
    font-size: 16px; color: var(--ink-light);
  }
</style>
</head>
<body>
<main class="canvas">

  <section class="card card--front" aria-label="Business card, contact side">
    <svg class="card__panel" viewBox="0 0 700 400" width="700" height="400" aria-hidden="true">
      <polygon points="322,0 700,0 700,400 258,400" fill="var(--navy)"/>
      <polygon points="311,0 322,0 258,400 247,400" fill="var(--grey)"/>
    </svg>

    <div class="brand">
      <span class="brand__dot"></span>
      <span class="brand__name">Ward Compass</span>
    </div>

    <div class="details">
      <h1 class="details__name">Salma Derkaoui</h1>
      <p class="details__role">CEO</p>
      <ul class="contact">
        <li class="contact__item">+90 612 348 2071
          <svg class="contact__icon" viewBox="0 0 24 24"><path d="M6.6 10.8a15.1 15.1 0 0 0 6.6 6.6l2.2-2.2a1 1 0 0 1 1-.25 11.4 11.4 0 0 0 3.6.57 1 1 0 0 1 1 1V20a1 1 0 0 1-1 1A17 17 0 0 1 3 4a1 1 0 0 1 1-1h3.5a1 1 0 0 1 1 1c0 1.25.2 2.45.57 3.57a1 1 0 0 1-.25 1z"/></svg>
        </li>
        <li class="contact__item">info@wardcompass-example.com
          <svg class="contact__icon" viewBox="0 0 24 24"><path d="M2 5h20v14H2z M2 5l10 8 10-8" fill="none" stroke="var(--grey)" stroke-width="2.4"/></svg>
        </li>
        <li class="contact__item">www.wardcompass-example.com
          <svg class="contact__icon" viewBox="0 0 24 24"><circle cx="12" cy="12" r="10" fill="none" stroke="var(--grey)" stroke-width="2.2"/><path d="M2 12h20M12 2c3 3 3 17 0 20M12 2c-3 3-3 17 0 20" fill="none" stroke="var(--grey)" stroke-width="1.8"/></svg>
        </li>
      </ul>
    </div>
    <p class="details__address">14 Annakhil 3 H.R.B. Rabat, Morocco</p>
  </section>

  <section class="card card--back" aria-label="Business card, brand side">
    <div class="brand">
      <span class="brand__dot"></span>
      <span class="brand__name">Ward Compass</span>
    </div>
  </section>

</main>
</body>
</html>
```